DL Flyer for vehicle buying/selling service and advice business

New business to help people sell their current vehicle then select and buy and maintain their next car. (New or used).
We'll prepare and sell your car for you and get $,000s more than a trade in.
Offer advice as to the best car currently on the market based on our customer's needs.
With country wide sourcing network of cars across all manufacturers we have great buying power to ensure the very best possible price.
Personal service, including preparation of car for sale, pickup of old and drop-off of new vehicles, organise RWC and any required repairs.
We are NOT a car dealer so we WILL not try to sell you the vehicles we own.
Totally impartial, professional and friendly service making the purchase of your next car a great experience.
Updates

Flyer wording===========“Don’t sell your car or buy your next car without speaking to us”We guarantee to get you a better price for your current car and to find a cheaper purchase price for your next car.With a country wide sourcing network of cars “new and used” across all manufacturers we have sensational buying power to ensure the very best possible price.We can source the right car on any budget, from $2,000 to $200,000We are NOT a car dealer so we WILL not try to sell you the vehicles we own.By not being affiliated with any individual car manufacturer or dealer we can offer absolute impartiality.We’ll sit with you to discuss the best car for your needs and even bring the car to you for a test drive without the pressure of a salesperson nearby.Our services include:• Selling your current car: - Obtaining a roadworthy certificate - Organising any repairs needed - Detailing your car (wash, vacuum, polish) - Advertising of your car - Dealing with potential buyers - Negotiating the best price on your behalf• Assisting with the selection of your next car• Organising test drives• Purchasing the car of your choice - Sourcing the very best price• Ongoing management of their vehicle (service, clean, repair)Possible inclusions in the flyer might be:Advantages of upgrading to a new vehicle include:o reliability, o safety,o fuel efficiencyo comfort.Space for a couple of short testimonials Background images of all of the major car manufacturers Added Friday, July 29, 2016

Target Market(s)

Local community.
Initially will drop DL flyers in local post boxes

Industry/Entity Type

Business

Requirements
Must have
• Flyer wording:
• ===========
• “Don’t sell your car or buy your next car without speaking to us”
• ---------------------------------------------------------------------------------
• We guarantee to get you a better price for your current car and to find a cheaper purchase price for your next car.
• With a country wide sourcing network of cars “new and used” across all manufacturers we have sensational buying power to ensure the very best possible price.
• We can source the right car on any budget, from $2,000 to $200,000
• We are NOT a car dealer so we WILL not try to sell you the vehicles we own.
• By not being affiliated with any individual car manufacturer or dealer we can offer absolute impartiality.
• We’ll sit with you to discuss the best car for your needs and even bring the car to you for a test drive without the pressure of a salesperson nearby.
• Our services include:
• • Selling your current car:
• o Obtaining a roadworthy certificate
• o Organising any repairs needed
• o Detailing your car (wash, vacuum, polish)
• o Advertising of your car
• o Dealing with potential buyers
• o Negotiating the best price on your behalf
• • Assisting with the selection of your next car
• • Organising test drives
• • Purchasing the car of your choice
• o Sourcing the very best price
• • Ongoing management of your vehicle (service, clean, repair)
• Call Gerald on: 0427 315064
Nice to have
• Possible inclusions on the flyer might be:
• List of advantages of upgrading to a new vehicle:
• o reliability,
• o safety,
• o fuel efficiency
• o comfort
• Space for a couple of short testimonials
• Background images of all of the major car manufacturers

```html
<!DOCTYPE html>
<html lang="en">
<head>
<meta charset="utf-8">
<title>DRV Vehicle Brokerage – DL Flyer</title>
<link rel="stylesheet" href="https://fonts.googleapis.com/css2?family=Open+Sans:ital,wght@0,400;0,600;0,700;1,400&family=Oswald:wght@500;600&display=swap">
<style>
:root{
  --orange:#f26f21;
  --charcoal:#4a4a4c;
  --charcoal-dark:#3a3a3c;
  --ink:#333335;
  --paper:#ffffff;
  --stage:#e9e7e4;
  --badge:#b9b9bc;
}
*{box-sizing:border-box;margin:0;padding:0}
html,body{width:1200px;height:989px;overflow:hidden;background:var(--stage)}
body{position:relative;font-family:"Open Sans",Arial,sans-serif;color:var(--ink)}
.flyer{position:absolute;width:400px;height:838px;overflow:hidden;background:var(--paper);box-shadow:0 4px 14px rgba(0,0,0,.18)}
.flyer--front{left:170px;top:60px}
.flyer--back{left:630px;top:90px}
.flyer__shapes{position:absolute;inset:0}
.abs{position:absolute}

/* front */
.brand{font-family:"Open Sans",Arial,sans-serif;font-weight:700;letter-spacing:7px;color:var(--ink)}
.front-brand{left:28px;top:2px;font-size:46px}
.front-tagline{left:163px;top:10px;font-size:13.5px;line-height:19px;color:#222}
.dealer-badge{left:254px;top:228px;width:116px;height:116px;border-radius:50%;background:var(--charcoal-dark);border:4px solid var(--orange);display:flex;align-items:center;justify-content:center;text-align:center;font-family:"Oswald",sans-serif;font-weight:500;font-size:10.5px;line-height:14px;color:#fff;text-transform:uppercase}
.hl{color:var(--orange)}
.headline{left:0;width:400px;top:349px;text-align:center;font-family:"Oswald",sans-serif;font-weight:500;font-size:17px;line-height:22px;color:var(--orange);text-transform:uppercase}
.promises{left:20px;top:414px;width:362px;list-style:none;color:#fff;font-size:9.4px;line-height:12.4px}
.promises li{position:relative;padding-left:14px;margin-bottom:6px;text-align:justify}
.promises li::before{content:"";position:absolute;left:1px;top:1px;width:4px;height:7px;border-right:2px solid var(--orange);border-bottom:2px solid var(--orange);transform:rotate(40deg)}
.tab{height:23px;background:var(--orange);color:#fff;font-family:"Oswald",sans-serif;font-weight:500;font-size:13px;line-height:23px;text-transform:uppercase;padding-left:14px;border-radius:0 12px 12px 0}
.advantages-tab{left:0;top:592px;width:326px}
.advantages{left:14px;top:621px;width:230px;display:grid;grid-template-columns:108px 120px;row-gap:3px;list-style:none;color:#fff;font-size:12.5px}
.dot-list li{position:relative;padding-left:16px}
.dot-list li::before{content:"";position:absolute;left:0;top:5px;width:9px;height:9px;border-radius:50%;background:var(--orange)}
.service-tab{left:274px;top:689px;width:126px;height:20px;line-height:20px;font-size:11px;padding-left:30px;border-radius:10px 0 0 10px}
.service-copy{left:190px;top:712px;width:196px;text-align:right;color:#fff;font-size:11px;line-height:14.5px}
.front-cta{left:20px;top:764px;font-size:14px;line-height:18px;color:var(--ink);font-weight:600}
.phone{color:var(--orange);font-weight:700;display:inline-flex;align-items:center;gap:4px}
.phone svg{width:12px;height:12px}

/* back */
.back-brand{right:32px;top:296px;font-size:44px;color:#fff}
.services-tab{left:0;top:365px;width:168px;height:23px;border-radius:0 12px 12px 0}
.services{left:14px;top:394px;width:380px;list-style:none;color:#fff}
.services > li{font-size:12.6px;line-height:18px;margin-top:2px}
.services .sub{list-style:none;margin-left:-14px;font-size:9.6px;line-height:12.4px;margin-top:1px}
.services .sub li::before{content:"• "}
.testimonial{left:20px;top:608px;width:360px;text-align:center;font-style:italic;font-size:9.6px;line-height:12.5px;color:#e6e6e6}
.back-cta{left:48px;top:664px;width:296px;height:54px;border:2px solid var(--orange);border-radius:12px;text-align:center;color:#fff;font-size:17px;line-height:21px;padding-top:5px;font-weight:600}
.back-cta .phone svg{width:15px;height:15px}
.maker-strip{left:0;top:733px;width:400px;height:105px;background:#fff;display:grid;grid-template-columns:repeat(14,1fr);align-items:center;justify-items:center;padding:8px 6px}
.maker-strip span{width:18px;height:18px;border-radius:50%;background:var(--badge)}
.maker-strip span:nth-child(3n){border-radius:3px;width:20px;height:14px}
</style>
</head>
<body>

<section class="flyer flyer--front" aria-label="Front of flyer">
  <svg class="flyer__shapes" viewBox="0 0 400 838" width="400" height="838" aria-hidden="false">
    <defs>
      <linearGradient id="carShot" x1="0" y1="0" x2="1" y2="1">
        <stop offset="0" stop-color="#8f9aa5"/>
        <stop offset=".45" stop-color="#c53a22"/>
        <stop offset="1" stop-color="#5c5f66"/>
      </linearGradient>
      <linearGradient id="workShot" x1="0" y1="0" x2="1" y2="1">
        <stop offset="0" stop-color="#9aa0a6"/><stop offset="1" stop-color="#3f4348"/>
      </linearGradient>
    </defs>
    <rect x="0" y="290" width="400" height="548" fill="var(--charcoal)"/>
    <path role="img" aria-label="Photo of a red hatchback car driving at speed" d="M0,86 C120,58 280,54 400,92 L400,302 C300,280 150,300 0,305 Z" fill="url(#carShot)"/>
    <path d="M0,80 C120,50 280,46 400,86 L400,94 C280,58 120,62 0,90 Z" fill="var(--orange)"/>
    <path d="M0,300 C150,298 300,278 400,298 L400,318 C300,300 160,335 0,342 Z" fill="var(--orange)"/>
    <path d="M0,745 C110,735 230,792 400,806 L400,838 L0,838 Z" fill="#f4f4f4"/>
    <path d="M0,745 C110,735 230,792 400,806" fill="none" stroke="var(--charcoal-dark)" stroke-width="3"/>
    <circle cx="66" cy="713" r="46" fill="url(#workShot)" stroke="var(--orange)" stroke-width="4" role="img" aria-label="Photo of a mechanic working on an engine"/>
    <circle cx="140" cy="731" r="32" fill="url(#workShot)" stroke="var(--orange)" stroke-width="3" role="img" aria-label="Photo of a car being polished"/>
  </svg>

  <div class="abs brand front-brand">DRV</div>
  <div class="abs front-tagline">NEW (FULL SERVICE) VEHICLE<br>BROKERAGE BUSINESS</div>

  <div class="abs dealer-badge"><p>We are <span class="hl">not</span> a<br>car dealer<br>so we <span class="hl">will</span> not<br>try to sell you the<br>vehicles we own</p></div>

  <h1 class="abs headline">Don’t sell your car or buy your next car<br>without speaking to us</h1>

  <ul class="abs promises">
    <li>We guarantee to get you a better price for your current car and to find a cheaper purchase price for your next car.</li>
    <li>With a country wide sourcing network of cars “new and used” across all manufacturers we have sensational buying power to ensure the very best possible price.</li>
    <li>We can source the right car on any budget, from $2,000 to $200,000</li>
    <li>We are NOT a car dealer so we WILL not try to sell you the vehicles we own.</li>
    <li>By not being affiliated with any individual car manufacturer or dealer we can offer absolute impartiality.</li>
    <li>We’ll sit with you to discuss the best car for your needs and even bring the car to you for a test drive without the pressure of a salesperson nearby.</li>
  </ul>

  <h2 class="abs tab advantages-tab">List of advantages of upgrading to a new vehicle</h2>
  <ul class="abs advantages dot-list">
    <li>Reliability</li><li>Fuel Efficiency</li>
    <li>Safety</li><li>Comfort</li>
  </ul>

  <h2 class="abs tab service-tab">DRV Full Service</h2>
  <p class="abs service-copy">Professional and friendly service making the purchase of your next car a great experience.</p>

  <p class="abs front-cta">Call Gerald on<br>
    <span class="phone"><svg viewBox="0 0 24 24"><path fill="currentColor" d="M6.6 10.8a15.1 15.1 0 0 0 6.6 6.6l2.2-2.2a1 1 0 0 1 1-.25 11.4 11.4 0 0 0 3.6.57 1 1 0 0 1 1 1V20a1 1 0 0 1-1 1A17 17 0 0 1 3 4a1 1 0 0 1 1-1h3.5a1 1 0 0 1 1 1c0 1.25.2 2.45.57 3.57a1 1 0 0 1-.25 1z"/></svg>0427 315064</span><br>
    to discuss your requirements</p>
</section>

<section class="flyer flyer--back" aria-label="Back of flyer">
  <svg class="flyer__shapes" viewBox="0 0 400 838" width="400" height="838">
    <defs>
      <linearGradient id="driverShot" x1="0" y1="0" x2="1" y2="1">
        <stop offset="0" stop-color="#e9e9e9"/><stop offset=".6" stop-color="#b9b9bb"/><stop offset="1" stop-color="#5b5d60"/>
      </linearGradient>
    </defs>
    <rect x="0" y="0" width="400" height="838" fill="var(--charcoal)"/>
    <path role="img" aria-label="Photo of a smiling driver at the wheel of a car interior" d="M0,0 H400 V288 C300,268 180,290 0,305 Z" fill="url(#driverShot)"/>
    <path d="M0,300 C170,290 300,260 400,292 L400,306 C300,284 170,330 0,344 Z" fill="var(--orange)"/>
    <rect x="0" y="727" width="400" height="6" fill="var(--orange)"/>
  </svg>

  <div class="abs brand back-brand">DRV</div>

  <h2 class="abs tab services-tab">Services we provide</h2>
  <ul class="abs services dot-list">
    <li>Selling your current car:
      <ul class="sub">
        <li>Obtaining a roadworthy certificate</li>
        <li>Organising any repairs needed</li>
        <li>Detailing your car (wash, vacuum, polish)</li>
        <li>Advertising of your car</li>
        <li>Dealing with potential buyers</li>
        <li>Negotiating the best price on your behalf</li>
      </ul>
    </li>
    <li>Assisting with the selection of your next car</li>
    <li>Organising test drives</li>
    <li>Purchasing the car of your choice
      <ul class="sub"><li>Sourcing the very best price</li></ul>
    </li>
    <li style="margin-top:8px">Ongoing management of your vehicle (service, clean, repair)</li>
  </ul>

  <blockquote class="abs testimonial">“Thanks Gerald for your wonderful advice! You take the hard work out of buying a car for people like me, who know nothing about cars and I am very grateful for your help.”<br>- Rosalind</blockquote>

  <div class="abs back-cta">Call Gerald on <span class="phone"><svg viewBox="0 0 24 24"><path fill="currentColor" d="M6.6 10.8a15.1 15.1 0 0 0 6.6 6.6l2.2-2.2a1 1 0 0 1 1-.25 11.4 11.4 0 0 0 3.6.57 1 1 0 0 1 1 1V20a1 1 0 0 1-1 1A17 17 0 0 1 3 4a1 1 0 0 1 1-1h3.5a1 1 0 0 1 1 1c0 1.25.2 2.45.57 3.57a1 1 0 0 1-.25 1z"/></svg>0427 315064</span><br>to discuss your requirements</div>

  <div class="abs maker-strip" role="img" aria-label="Row of car manufacturer badges">
    <span></span><span></span><span></span><span></span><span></span><span></span><span></span><span></span><span></span><span></span><span></span><span></span><span></span><span></span>
    <span></span><span></span><span></span><span></span><span></span><span></span><span></span><span></span><span></span><span></span><span></span><span></span><span></span><span></span>
    <span></span><span></span><span></span><span></span><span></span><span></span><span></span><span></span><span></span><span></span><span></span><span></span><span></span><span></span>
  </div>
</section>

</body>
</html>
```